Need a business card design. I am a Self Empowerment Life Coach.

A Life Coach is - a professional relationship designed to enhance an individual's ability to focus, make effective changes, develop oneself, achieve desired goals and maximize success in life. Coaching is about getting the very best out of someone and enabling them to make decisions that will improve their life. It is a unique way to help people look at where they are now and where they would like to be, and helps bridge the gap.

Tidal Grove Coaching is motivational, inspiring, positive, exciting and action driven. By raising awareness and encouraging others to take responsibility for their life, coaching can help people rise to their challenge and go further than you ever thought possible.

Industry/Entity Type

Business

Font styles to use
Other font styles liked:
• Bookman Old Style

Requirements
Must have
• Marlena Voskuil, ELI-MP
• Self Empowerment Coach
• 358.617.2083
• mv@thebrightpathguide.net
• The attached logo
Nice to have
• I would like to see some designs portrait and some landscape

```html
<!DOCTYPE html>
<html lang="en">
<head>
<meta charset="UTF-8">
<title>Tidal Grove Coaching – Business Card</title>
<link rel="stylesheet" href="https://fonts.googleapis.com/css2?family=Open+Sans:wght@400;600;700&display=swap">
<style>
  :root {
    --stage-bg: #e9ebef;
    --card-white: #ffffff;
    --navy: #1d3f84;
    --navy-deep: #15316b;
    --sky: #1a9ad8;
    --ink: #4a4f57;
    --divider: #c9ccd2;
    --sun-light: #ffe36a;
    --sun-deep: #f5b000;
  }
  * { box-sizing: border-box; margin: 0; padding: 0; }
  html, body { width: 1200px; height: 750px; overflow: hidden; }
  body {
    background: var(--stage-bg);
    font-family: "Open Sans", Arial, sans-serif;
    position: relative;
  }
  .card {
    position: absolute;
    top: 220px;
    width: 540px;
    height: 310px;
    border-radius: 16px;
    background: var(--card-white);
    overflow: hidden;
    box-shadow: 0 6px 18px rgba(0,0,0,.12);
  }
  .card--front { left: 40px; }
  .card--back { left: 620px; }

  /* Front */
  .front-artwork {
    position: absolute;
    left: 30px; top: 24px;
    width: 370px; height: 262px;
    border-radius: 12px;
    background: radial-gradient(circle at 40% 40%, var(--sun-light), var(--sun-deep) 70%, #f3f3f3 100%);
  }
  .brand {
    position: absolute;
    display: flex;
    align-items: center;
    gap: 6px;
    color: var(--navy);
    font-weight: 700;
    line-height: 1.1;
  }
  .brand__dot {
    flex: none;
    border-radius: 50%;
    background: var(--sun-deep);
  }
  .card--front .brand { left: 414px; top: 70px; width: 112px; font-size: 15px; }
  .card--front .brand__dot { width: 14px; height: 14px; }

  /* Back */
  .back-bands { position: absolute; inset: 0; }
  .holder {
    position: absolute;
    right: 28px; top: 60px;
    text-align: right;
    color: #fff;
  }
  .holder__name { font-size: 19px; font-weight: 700; letter-spacing: .2px; }
  .holder__title { font-size: 13px; font-weight: 400; margin-top: 2px; }

  .card--back .brand { left: 34px; top: 222px; width: 150px; font-size: 17px; }
  .card--back .brand__dot { width: 18px; height: 18px; }
  .back-divider {
    position: absolute;
    left: 196px; top: 186px;
    width: 1px; height: 104px;
    background: var(--divider);
  }
  .contacts {
    position: absolute;
    left: 222px; top: 196px;
    list-style: none;
    color: var(--ink);
    font-size: 12.5px;
  }
  .contacts li { display: flex; align-items: center; gap: 8px; height: 21px; }
  .contacts svg { width: 13px; height: 13px; flex: none; }
</style>
</head>
<body>

<section class="card card--front" aria-label="Card front">
  <div class="front-artwork" role="img" aria-label="Playful yellow and white cartoon illustration"></div>
  <div class="brand"><span class="brand__dot"></span><span>Tidal Grove Coaching</span></div>
</section>

<section class="card card--back" aria-label="Card back">
  <svg class="back-bands" viewBox="0 0 540 310" preserveAspectRatio="none" aria-hidden="true">
    <path d="M0,0 H540 V128 C420,112 220,130 0,226 Z" fill="var(--sky)"/>
    <path d="M0,0 H540 V118 C420,102 220,118 0,212 Z" fill="var(--navy)"/>
    <path d="M0,0 H540 V60 C420,70 250,60 0,150 Z" fill="var(--navy-deep)" opacity=".35"/>
  </svg>

  <div class="holder">
    <p class="holder__name">Marlena Voskuil, ELI-MP</p>
    <p class="holder__title">Self Empowerment Coach</p>
  </div>

  <div class="brand"><span class="brand__dot"></span><span>Tidal Grove Coaching</span></div>
  <div class="back-divider"></div>

  <ul class="contacts">
    <li>
      <svg viewBox="0 0 16 16" aria-hidden="true"><path d="M3 1h3l1.5 4-2 1.2a9 9 0 0 0 4.3 4.3l1.2-2 4 1.5v3a2 2 0 0 1-2 2A13 13 0 0 1 1 3a2 2 0 0 1 2-2z" fill="var(--navy)"/></svg>
      <span>358.617.2083</span>
    </li>
    <li>
      <svg viewBox="0 0 16 16" aria-hidden="true"><rect x="1" y="3" width="14" height="10" rx="1" fill="var(--navy)"/><path d="M1.5 3.5 8 9l6.5-5.5" fill="none" stroke="#fff" stroke-width="1.3"/></svg>
      <span>mv@thebrightpathguide.net</span>
    </li>
    <li>
      <svg viewBox="0 0 16 16" aria-hidden="true"><circle cx="8" cy="8" r="6.5" fill="none" stroke="var(--navy)" stroke-width="1.4"/><path d="M1.5 8h13M8 1.5c-3 3.5-3 9.5 0 13M8 1.5c3 3.5 3 9.5 0 13" fill="none" stroke="var(--navy)" stroke-width="1.1"/></svg>
      <span>www.thebrightpathguide.net</span>
    </li>
  </ul>
</section>

</body>
</html>
```